Design a upcoming mobile game webpage

I have a domain space up but as I am still needed to work on getting the content and every other things setup, I would like to at least populate the page with a coming soon page with videos/images or links to plumtalk,gx etc and a newsletter sign up.
It can be design as a full game site but to illustrate it as "Coming soon to you on IOS and Android"
Target Market(s)
Consumer who holds a mobile device
Industry/Entity Type
Android

```html
<!DOCTYPE html>
<html lang="en">
<head>
<meta charset="utf-8">
<title>Legend Ascendant — Coming Soon</title>
<link rel="stylesheet" href="https://fonts.googleapis.com/css2?family=Cinzel:wght@400;700&family=Marcellus&family=Lato:wght@400;700&family=Montserrat:wght@800&family=Orbitron:wght@700&display=swap">
<style>
  :root {
    --ink: #ffffff;
    --cave-deep: #06140f;
    --cave-mid: #1d3b32;
    --cave-glow: #d9c48a;
    --moss: #3b5a2a;
    --panel: rgba(0, 0, 0, 0.34);
    --box: rgba(0, 0, 0, 0.55);
    --box-border: #8a8f8c;
    --gold: #e9a83c;
    --desktop: #2a8ac2;
    --mobile: #6cb32a;
    --bar-text: #2a2a2a;
    --sky-light: #d6ebf7;
    --sky-dark: #5aa7d5;
    --field: #f3f3f3;
    --field-text: #9a9a9a;
    --hazard-yellow: #f2c418;
    --hazard-dark: #151515;
    --track: #444444;
    --track-border: #8d8d8d;
    --fire-a: #ff8a00;
    --fire-b: #ffef00;
  }
  * { box-sizing: border-box; margin: 0; padding: 0; }
  html, body { width: 1200px; height: 1000px; overflow: hidden; }
  body { position: relative; background: var(--cave-deep); color: var(--ink); font-family: "Lato", sans-serif; }

  .backdrop {
    position: absolute; inset: 0;
    background:
      radial-gradient(ellipse 420px 360px at 1030px 380px, rgba(233, 214, 160, 0.85), rgba(233, 214, 160, 0) 70%),
      radial-gradient(ellipse 700px 300px at 600px 200px, rgba(44, 110, 92, 0.55), rgba(44, 110, 92, 0) 70%),
      linear-gradient(180deg, #0b211a 0%, var(--cave-mid) 35%, #2b3a26 65%, #1a2216 85%, #0c0f0b 100%);
  }

  .site-title {
    position: absolute; top: 38px; left: 0; width: 1200px; text-align: center;
    font-family: "Cinzel", serif; font-weight: 400; font-size: 74px; letter-spacing: 3px; line-height: 1;
  }

  .visitors {
    position: absolute; left: 144px; top: 199px; width: 381px; height: 209px;
    background: var(--box); border: 1px solid var(--box-border); border-radius: 9px; text-align: center;
  }
  .visitors__label { margin-top: 8px; font-family: "Cinzel", serif; font-size: 26px; color: var(--gold); font-variant: small-caps; }
  .visitors__count { font-family: "Marcellus", serif; font-size: 46px; line-height: 1.05; margin-top: 2px; }
  .visitors__caption { font-family: "Marcellus", serif; font-size: 18px; margin-top: 4px; }
  .split__labels { position: absolute; top: 150px; left: 4px; width: 374px; height: 20px; font-size: 15px; }
  .split__labels span { position: absolute; }
  .split__labels .is-desktop { left: 91px; }
  .split__labels .is-mobile { left: 282px; }
  .split { position: absolute; left: 4px; top: 174px; width: 374px; height: 26px; display: flex; }
  .split__part { display: flex; align-items: center; justify-content: center; font-family: "Marcellus", serif; font-size: 17px; color: var(--bar-text); }
  .split__part--desktop { width: 241px; background: var(--desktop); }
  .split__part--mobile { width: 133px; background: var(--mobile); }

  .newsletter {
    position: absolute; left: 587px; top: 332px; width: 521px; height: 68px;
    background: linear-gradient(180deg, var(--sky-light), var(--sky-dark));
  }
  .newsletter__field {
    position: absolute; left: 9px; top: 11px; width: 392px; height: 47px;
    border: 1px solid #c9c9c9; border-radius: 12px; background: var(--field);
    padding: 0 10px; font: 15px "Lato", sans-serif; color: #333;
  }
  .newsletter__field::placeholder { color: var(--field-text); }
  .newsletter__button {
    position: absolute; left: 409px; top: 11px; width: 102px; height: 47px;
    border: 1px solid #4f86a8; background: linear-gradient(180deg, #d4ebf8, #8fc5e6);
    font: 15px "Lato", sans-serif; color: #2a3a44;
  }

  .launch { position: absolute; left: 143px; top: 426px; width: 965px; height: 514px; background: var(--panel); }
  .caution {
    position: absolute; left: 0; top: 0; width: 965px; height: 69px;
    background: linear-gradient(180deg, #c9c9c9 0%, var(--hazard-yellow) 30%, #8a6d08 65%, var(--hazard-dark) 100%);
  }
  .caution__label {
    position: absolute; left: 202px; top: 11px; width: 562px; height: 47px; border-radius: 7px;
    background: rgba(30, 24, 8, 0.72);
    font-family: "Montserrat", sans-serif; font-weight: 800; font-size: 47px; line-height: 47px; text-align: center; letter-spacing: 0.5px;
  }

  .countdown { position: absolute; top: 114px; left: 0; width: 965px; }
  .countdown__digits { text-align: center; font-family: "Orbitron", sans-serif; font-weight: 700; font-size: 120px; line-height: 1; letter-spacing: 6px; }
  .countdown__units { position: absolute; top: 142px; left: 0; width: 965px; height: 40px; font-family: "Orbitron", sans-serif; font-weight: 700; font-size: 34px; }
  .countdown__units span { position: absolute; }

  .progress {
    position: absolute; left: 57px; top: 347px; width: 867px; height: 62px;
    background: var(--track); border: 1px solid var(--track-border); border-radius: 8px;
  }
  .progress__fill {
    position: absolute; left: 15px; top: 18px; width: 417px; height: 26px;
    background: linear-gradient(180deg, var(--fire-a), var(--fire-b) 50%, var(--fire-a));
    text-align: center; font-size: 18px; line-height: 26px; color: var(--bar-text);
  }

  .footer-strip { position: absolute; left: 0; top: 940px; width: 1200px; height: 60px; background: rgba(0, 0, 0, 0.35); }
  .copyright { position: absolute; left: 56px; top: 972px; font-family: "Cinzel", serif; font-size: 13px; }
</style>
</head>
<body>
  <div class="backdrop" role="img" aria-label="Fantasy illustration of a mossy cave with hanging stalactites opening onto a sunlit valley"></div>

  <h1 class="site-title">Legend Ascendant</h1>

  <section class="visitors">
    <p class="visitors__label">Visitors count</p>
    <p class="visitors__count">2,501</p>
    <p class="visitors__caption">Right Now</p>
    <div class="split__labels"><span class="is-desktop">Desktop</span><span class="is-mobile">Mobile</span></div>
    <div class="split">
      <div class="split__part split__part--desktop">66%</div>
      <div class="split__part split__part--mobile">34%</div>
    </div>
  </section>

  <form class="newsletter">
    <input class="newsletter__field" type="email" placeholder="Enter your Email to subscribe">
    <button class="newsletter__button" type="button">Subscribe</button>
  </form>

  <section class="launch">
    <div class="caution" role="img" aria-label="Yellow and black diagonal caution stripes">
      <h2 class="caution__label">COMING SOON</h2>
    </div>

    <div class="countdown">
      <div class="countdown__digits">21:15:52:29</div>
      <div class="countdown__units">
        <span style="left:116px">DAYS</span>
        <span style="left:295px">HOURS</span>
        <span style="left:474px">MINUTES</span>
        <span style="left:690px">SECONDS</span>
      </div>
    </div>

    <div class="progress">
      <div class="progress__fill">50%</div>
    </div>
  </section>

  <div class="footer-strip"></div>
  <p class="copyright">Copyright © 2014. All Rights Reserved</p>
</body>
</html>
```